Stationary for Manufacturing Company
Metal Manufacturing
Stationary for Manufacturing Company - Manufacturing
Creative Brief
Professional
Gerald Pinwick
27615 Harlow Ave Unit C Longmont, CO 80519
gpinwick@forgevx.com
www.forgevx.com
Would like stationary designs following our logo design.
gpinwick gpinwick
quillmotions I like #79 & #87 with the solid color. Can you do a these on other stationary objects.
Nook, I really like the stationary on #88 & #89, can you continue the design onto the inside of the folder on the pockets. Also I would like to see Forge Vexa in shading in smaller text like #16 and the large shaded logo removed. Thank you for your submissions.
#129 & #126 I like both of these cards, #129 seems to have to many lines and seems to busy. Can you reduce some of them and do this on other stationary objects as well. Thank you.
#16 I really like how the text Forge Vexa is on the back of the card.Can you put that one in other stationary objects as well. Thank you.

```html
<!DOCTYPE html>
<html lang="en">
<head>
<meta charset="utf-8">
<title>Forge Vexa Business Card</title>
<link href="https://fonts.googleapis.com/css2?family=Open+Sans:wght@400;600;700&display=swap" rel="stylesheet">
<style>
  :root {
    --bg: #e9eaec;
    --brand-blue: #3b6fb6;
    --brand-blue-dark: #2a5696;
    --card-white: #ffffff;
    --panel-dark: #333438;
    --text-light: #f2f2f2;
  }
  * { margin: 0; padding: 0; box-sizing: border-box; }
  html, body { width: 1200px; height: 837px; overflow: hidden; }
  body {
    background: var(--bg);
    font-family: "Open Sans", Arial, sans-serif;
    position: relative;
  }
  .card {
    position: absolute;
    width: 520px;
    height: 297px;
    border-radius: 4px;
    box-shadow: 0 10px 28px rgba(0,0,0,0.18);
    overflow: hidden;
  }

  /* Front */
  .card-front {
    left: 90px;
    top: 450px;
    background: var(--brand-blue);
  }
  .front-panel {
    position: absolute;
    left: 20px;
    top: 20px;
    width: 420px;
    height: 257px;
    background: var(--card-white);
    border-radius: 14px;
    display: flex;
    flex-direction: column;
    align-items: center;
    justify-content: center;
  }
  .brand-mark {
    display: flex;
    align-items: center;
    gap: 10px;
  }
  .brand-dot {
    width: 26px;
    height: 26px;
    border-radius: 50%;
    background: var(--brand-blue);
  }
  .brand-name {
    font-size: 34px;
    font-weight: 700;
    color: var(--brand-blue);
    letter-spacing: 0.5px;
  }
  .brand-tagline {
    margin-top: 4px;
    font-size: 11px;
    font-weight: 600;
    letter-spacing: 2px;
    color: var(--brand-blue-dark);
    text-transform: uppercase;
  }
  .front-name {
    position: absolute;
    left: 440px;
    width: 80px;
    top: 20px;
    height: 257px;
    display: flex;
    align-items: flex-end;
    justify-content: center;
    padding-bottom: 0;
  }
  .front-name span {
    display: block;
    writing-mode: vertical-rl;
    transform: rotate(180deg);
    color: var(--card-white);
    font-weight: 700;
    font-size: 19px;
    white-space: nowrap;
  }

  /* Back */
  .card-back {
    left: 590px;
    top: 110px;
    background: var(--card-white);
  }
  .back-panel {
    position: absolute;
    left: 30px;
    top: 30px;
    width: 460px;
    height: 170px;
    background: var(--panel-dark);
    border-radius: 12px;
    padding: 0 24px 24px 24px;
    display: grid;
    grid-template-columns: auto auto;
    grid-auto-rows: 16px;
    align-content: end;
    justify-content: space-between;
    column-gap: 16px;
    row-gap: 12px;
  }
  .contact-row {
    display: flex;
    align-items: center;
    gap: 7px;
    color: var(--text-light);
    font-size: 10px;
    line-height: 16px;
    white-space: nowrap;
  }
  .contact-icon {
    width: 14px;
    height: 14px;
    flex: none;
  }
</style>
</head>
<body>

<section class="card card-back" aria-label="Business card back">
  <div class="back-panel">
    <div class="contact-row">
      <svg class="contact-icon" viewBox="0 0 14 14"><circle cx="7" cy="7" r="7" fill="#f2f2f2"/><path d="M7 3.2a2.4 2.4 0 0 0-2.4 2.4C4.6 7.4 7 10.6 7 10.6s2.4-3.2 2.4-5A2.4 2.4 0 0 0 7 3.2z" fill="#333438"/></svg>
      <span>27615 Harlow Ave Unit C Brennick, OR 97321</span>
    </div>
    <div class="contact-row">
      <svg class="contact-icon" viewBox="0 0 14 14"><circle cx="7" cy="7" r="7" fill="#f2f2f2"/><path d="M4.6 3.6l1.4-.2.7 1.8-.9.6a5 5 0 0 0 2.4 2.4l.6-.9 1.8.7-.2 1.4c-3.4.3-6.1-2.4-5.8-5.8z" fill="#333438"/></svg>
      <span>303-555-0187</span>
    </div>
    <div class="contact-row">
      <svg class="contact-icon" viewBox="0 0 14 14"><circle cx="7" cy="7" r="7" fill="#f2f2f2"/><path d="M4.6 3.6l1.4-.2.7 1.8-.9.6a5 5 0 0 0 2.4 2.4l.6-.9 1.8.7-.2 1.4c-3.4.3-6.1-2.4-5.8-5.8z" fill="#333438"/></svg>
      <span>303-555-0142</span>
    </div>
    <div class="contact-row">
      <svg class="contact-icon" viewBox="0 0 14 14"><circle cx="7" cy="7" r="7" fill="#f2f2f2"/><circle cx="7" cy="7" r="3.6" fill="none" stroke="#333438" stroke-width="1"/><path d="M3.4 7h7.2M7 3.4v7.2" stroke="#333438" stroke-width="0.8"/></svg>
      <span>www.forgevx.com</span>
    </div>
    <div class="contact-row">
      <svg class="contact-icon" viewBox="0 0 14 14"><circle cx="7" cy="7" r="7" fill="#f2f2f2"/><rect x="3.6" y="4.5" width="6.8" height="5" fill="none" stroke="#333438" stroke-width="1"/><path d="M3.6 4.5L7 7.3l3.4-2.8" fill="none" stroke="#333438" stroke-width="1"/></svg>
      <span>gpinwick@forgevx.com</span>
    </div>
  </div>
</section>

<section class="card card-front" aria-label="Business card front">
  <div class="front-panel">
    <div class="brand-mark">
      <span class="brand-dot"></span>
      <span class="brand-name">Forge Vexa</span>
    </div>
    <div class="brand-tagline">Shaping Steel Forward</div>
  </div>
  <div class="front-name"><span>Gerald Pinwick</span></div>
</section>

</body>
</html>
```